Brochure for people who suffer from Sleep Apnea and need a medical device called a CPAP Machine

I want a brochure that can be placed in doctors offices with my competitors brochures. It needs to be bold and stand out and deliver a very strong message that draws the patients away from our competitors and to us. I have included a word document generally outlining some of my requirements and thoughts, please review prior to investing time into design!

Target Market(s)

people who suffer from sleep apnea, which is a disease that causes them to stop breathing many times per hour, resulting in the patient needing to wear a device called a CPAP Machine. This is an illness that can impact anyone but is more likely to impact those suffering from obesity and men.

Industry/Entity Type

Health Care

Other font styles liked:
• Use what you think is best

Colors

Designer to choose colors to be used in the design.

Requirements
Must have
• Please see word document for must have items, and feel free to contact me with any questions.
• Also must have bold colors, and/or graphics to really stand out among my competitors brochures.
Nice to have
• Would prefer to use the baby picture titled "sleeping baby 4" if possible but provided 2 other baby photos just in case. Whatever you want to add, use your professional creativity! You Don't need to use all the pictures uploaded!!!!!
Should not have
• Nothing discriminatory or offensive.

```html
<!DOCTYPE html>
<html lang="en">
<head>
<meta charset="utf-8">
<title>NightEase CPAP – Tri-fold Brochure</title>
<link href="https://fonts.googleapis.com/css2?family=Barlow+Condensed:wght@400;500;600;700&family=Open+Sans:wght@400;600;700&display=swap" rel="stylesheet">
<style>
  :root{
    --purple:#8a4fa3;
    --purple-dark:#6e3a88;
    --green:#2fb36f;
    --white:#ffffff;
    --ink:#3a3a3a;
    --muted:#6d6d6d;
    --backdrop:#c9c9cb;
    --head:"Barlow Condensed", "Arial Narrow", sans-serif;
    --body:"Open Sans", Arial, sans-serif;
  }
  *{box-sizing:border-box;margin:0;padding:0}
  html,body{width:1200px;height:1000px;overflow:hidden}
  body{background:var(--backdrop);font-family:var(--body);color:var(--ink)}

  .sheet{position:absolute;left:210px;width:780px;height:460px;display:grid;grid-template-columns:repeat(3,260px);box-shadow:0 6px 18px rgba(0,0,0,.18)}
  .sheet--outside{top:20px}
  .sheet--inside{top:520px}
  .panel{position:relative;height:460px;overflow:hidden;background:var(--white)}
  .panel + .panel{border-left:1px solid #e6e6e6}
  .panel--purple{background:var(--purple);color:var(--white)}

  .head{font-family:var(--head);font-weight:600;text-transform:uppercase;line-height:1.05}
  .accent{color:var(--green)}
  .rule{display:block;width:16px;height:2px;background:var(--green);margin:8px 0}

  /* outside – services panel */
  .services{padding:24px 18px 0 18px}
  .services__intro{font-size:8.5px;line-height:1.55;margin-bottom:8px}
  .services__item{margin-bottom:10px}
  .services__title{font-size:8.5px;font-weight:600;text-transform:uppercase;letter-spacing:.2px}
  .services__desc{font-size:7.8px;line-height:1.5;padding-left:8px;opacity:.95}
  .services__footer{position:absolute;left:0;right:0;bottom:0;height:82px;background:var(--white);border-top:2px solid var(--green);padding:14px 18px 0;color:var(--purple)}
  .services__footer .head{font-size:16px;font-weight:600}
  .services__footer .underline{color:var(--green);font-weight:500;border-bottom:1.5px solid var(--green)}
  .services__tag{margin-top:8px;font-size:8px;font-weight:600;color:var(--ink)}

  /* brand */
  .brand{display:flex;align-items:center;justify-content:center;gap:5px;padding-top:16px;height:48px}
  .brand__dot{width:8px;height:8px;border-radius:50%;background:var(--green)}
  .brand__name{font-family:var(--head);font-weight:600;font-size:17px;color:var(--purple)}

  /* hero band */
  .hero{position:relative;height:180px}
  .hero__band{position:absolute;left:0;right:0;top:46px;bottom:0;background:var(--purple)}
  .hero__curve{position:absolute;left:0;bottom:-1px;width:260px;height:14px}
  .hero__photo{position:absolute;left:35px;top:0;width:190px;height:104px}
  .hero__text{position:absolute;left:30px;right:18px;top:114px;color:var(--white)}
  .hero__text .head{font-size:16px}
  .hero__text p{font-size:7.5px;margin-top:4px;opacity:.9}
  .photo-couple{background:linear-gradient(135deg,#e9e4df,#c9b9ab 55%,#8f7b6d)}
  .photo-baby{background:radial-gradient(ellipse at 45% 55%,#f3d8c6 0%,#e8c2aa 45%,#f4f1ee 80%)}

  /* guarantee + contact */
  .guarantee{display:flex;gap:10px;padding:22px 18px 0 30px;align-items:flex-start}
  .badge{flex:none;width:46px;height:34px}
  .guarantee p{font-family:var(--head);font-size:11px;color:var(--purple);text-transform:uppercase;line-height:1.15}
  .guarantee strong{font-weight:700}
  .contact{padding:22px 18px 0 30px}
  .contact .head{font-size:13px;font-weight:500;color:var(--purple)}
  .contact .head strong{color:var(--green);font-weight:600}
  .address{margin-top:18px;font-size:7.5px;line-height:1.7}
  .address .phone{color:var(--purple)}
  .address .region{margin-top:12px}
  .address .web{color:var(--purple)}

  /* outside – difference panel */
  .diff{padding:16px 18px 0 30px}
  .diff .head{font-size:16px;color:var(--purple)}
  .diff .accent{font-family:var(--head);font-size:11px;font-weight:500;text-transform:uppercase;margin-top:2px}
  .checklist{list-style:none;margin-top:12px}
  .checklist li{display:flex;align-items:center;gap:6px;font-size:7.3px;line-height:1.7}
  .checklist svg{width:7px;height:7px;flex:none}
  .store{margin-top:10px;font-family:var(--head);font-size:12px;font-weight:500;color:var(--green);text-transform:uppercase}
  .big-phone{font-family:var(--head);font-size:19px;font-weight:600;color:var(--purple);margin-top:1px;line-height:1.1}
  .diff .web{font-size:7.5px;color:var(--purple);margin-top:3px}
  .strip{position:absolute;left:0;right:0;bottom:0;height:10px;background:var(--purple)}

  /* inside */
  .spread-photo{position:absolute;z-index:2;top:22px;left:20px;width:500px;height:270px;background:linear-gradient(100deg,#2e3846 0%,#5b5e66 35%,#b6a99a 60%,#d6cbbb 100%)}
  .inside-copy{position:absolute;top:310px;left:22px;right:18px;bottom:0}
  .inside-copy .head{font-size:16px;color:var(--purple);line-height:1.1}
  .inside-copy .link{color:var(--green);text-decoration:underline}
  .inside-copy .note{font-size:7.5px;line-height:1.6;margin-top:8px}
  .inside-copy .web{position:absolute;bottom:14px;left:0;font-size:7px;color:var(--purple)}
  .talk .sub{font-family:var(--head);font-size:12px;font-weight:500;color:var(--purple);text-transform:uppercase;line-height:1.25;margin-top:4px}
  .talk .sub strong{font-weight:700}
  .talk .brand{justify-content:flex-start;padding-top:12px}

  .help{padding:40px 20px 0 22px}
  .help .head{font-size:18px;font-weight:600}
  .help__label{font-family:var(--head);font-size:12px;text-transform:uppercase;line-height:1.3;margin-top:26px}
  .help__label strong{font-weight:700}
  .help ul{list-style:none;margin-top:16px}
  .help li{font-size:7.4px;line-height:1.6;margin-bottom:12px;padding-left:9px;position:relative}
  .help li::before{content:"";position:absolute;left:0;top:5px;width:3px;height:3px;border-radius:50%;background:var(--white)}
  .help__call{position:absolute;left:22px;bottom:28px}
  .help__call span{font-size:10px}
  .help__call .big-phone{color:var(--white);font-size:24px}
</style>
</head>
<body>

<!-- OUTSIDE -->
<section class="sheet sheet--outside">

  <article class="panel panel--purple">
    <div class="services">
      <p class="services__intro">Anyone can give you CPAP Supplies. However we are committed to providing you with exceptional customer service too.</p>
      <p class="services__intro">How do we do this? By giving you services no other CPAP retailer offers, like....</p>
      <span class="rule"></span>
      <div class="services__item"><p class="services__title">...Free home visits:</p><p class="services__desc">We bring the store to you so we can give you as much time you need and set up all you equipment and supplies for you.</p></div>
      <div class="services__item"><p class="services__title">...Free delivery:</p><p class="services__desc">So you never need to come to the store (Unless you want to!).</p></div>
      <div class="services__item"><p class="services__title">...Night and weekend appointments:</p><p class="services__desc">Because not everyone works 9-to-5.</p></div>
      <div class="services__item"><p class="services__title">...A dedicated clinician:</p><p class="services__desc">Because we also want to be your friend.</p></div>
      <div class="services__item"><p class="services__title">...Hardship and financial-assistance programs:</p><p class="services__desc">To make sure everyone gets the care they need.</p></div>
      <div class="services__item"><p class="services__title">...Promise of guaranteed success:</p><p class="services__desc">We offer 30-day guarantees on all supplies so you know you are getting the best care possible.</p></div>
    </div>
    <div class="services__footer">
      <p class="head">Why are you settling<br>for less? <span class="underline">Let us treat you right!</span></p>
      <p class="services__tag">We Make <span class="accent">CPAP</span> Personal!</p>
    </div>
  </article>

  <article class="panel">
    <div class="brand"><span class="brand__dot"></span><span class="brand__name">NightEase CPAP</span></div>
    <div class="hero">
      <div class="hero__band"></div>
      <div class="hero__photo photo-couple" role="img" aria-label="Photo of a couple in bed, one wearing a CPAP mask"></div>
      <div class="hero__text">
        <p class="head">CPAP doesn't need to<br>be like this!</p>
        <p>Let us make sure this doesn't happen to you.</p>
      </div>
      <svg class="hero__curve" viewBox="0 0 260 14" preserveAspectRatio="none"><path d="M0 14 Q130 0 260 10 L260 14 Z" fill="#fff"/><path d="M0 13 Q130 -1 260 9" fill="none" stroke="#2fb36f" stroke-width="1.2"/></svg>
    </div>
    <div class="guarantee">
      <svg class="badge" viewBox="0 0 46 34" role="img" aria-label="Satisfaction guarantee seal"><rect x="2" y="13" width="42" height="9" fill="#b3261e"/><circle cx="23" cy="17" r="13" fill="#e0a526"/><circle cx="23" cy="17" r="9" fill="#f3c84b"/></svg>
      <p>We guarantee your <strong>CPAP success</strong>, because your success is our reputation.</p>
    </div>
    <div class="contact">
      <p class="head">Call for an appointment (or just to talk) <strong>today!!!</strong></p>
      <div class="address">
        <p>NightEase CPAP</p>
        <p class="phone">555-014-2290</p>
        <p>48 Maple Lane</p>
        <p>Fairview, Ontario L0X 1A0</p>
        <p class="region">Serving all of Ontario</p>
        <p class="web">www.NightEaseCPAP.com</p>
      </div>
    </div>
  </article>

  <article class="panel">
    <div class="brand"><span class="brand__dot"></span><span class="brand__name">NightEase CPAP</span></div>
    <div class="hero">
      <div class="hero__band"></div>
      <div class="hero__photo photo-baby" role="img" aria-label="Photo of a smiling sleeping baby"></div>
      <div class="hero__text">
        <p class="head">Want sleep like a baby<br>again? <span style="font-weight:400">Let us show how!</span></p>
        <p>Serving all of Ontario.</p>
      </div>
      <svg class="hero__curve" viewBox="0 0 260 14" preserveAspectRatio="none"><path d="M0 14 Q130 0 260 10 L260 14 Z" fill="#fff"/><path d="M0 13 Q130 -1 260 9" fill="none" stroke="#2fb36f" stroke-width="1.2"/></svg>
    </div>
    <div class="diff">
      <p class="head">What makes us<br>different?</p>
      <p class="accent">Everything!</p>
      <ul class="checklist">
        <li><svg viewBox="0 0 8 8"><path d="M1 4.2 3 6.2 7 1.6" fill="none" stroke="#2fb36f" stroke-width="1.4"/></svg>Free Home Visits</li>
        <li><svg viewBox="0 0 8 8"><path d="M1 4.2 3 6.2 7 1.6" fill="none" stroke="#2fb36f" stroke-width="1.4"/></svg>Free delivery</li>
        <li><svg viewBox="0 0 8 8"><path d="M1 4.2 3 6.2 7 1.6" fill="none" stroke="#2fb36f" stroke-width="1.4"/></svg>Night and weekend appointments</li>
        <li><svg viewBox="0 0 8 8"><path d="M1 4.2 3 6.2 7 1.6" fill="none" stroke="#2fb36f" stroke-width="1.4"/></svg>Specializes exclusively in Sleep Therapy</li>
        <li><svg viewBox="0 0 8 8"><path d="M1 4.2 3 6.2 7 1.6" fill="none" stroke="#2fb36f" stroke-width="1.4"/></svg>A dedicated clinician assigned directly to you</li>
        <li><svg viewBox="0 0 8 8"><path d="M1 4.2 3 6.2 7 1.6" fill="none" stroke="#2fb36f" stroke-width="1.4"/></svg>Hardship and financial-assistance programs</li>
      </ul>
      <p class="store">We bring the store to you</p>
      <p class="big-phone">555-014-2290</p>
      <p class="web">www.NightEaseCPAP.com</p>
    </div>
    <div class="strip"></div>
  </article>
</section>

<!-- INSIDE -->
<section class="sheet sheet--inside">
  <div class="spread-photo" role="img" aria-label="Photo of a woman with closed eyes breathing deeply outdoors"></div>

  <article class="panel">
    <div class="inside-copy">
      <p class="head">There are many resources available for you on our website at <span class="link">www.NightEaseCPAP.com.</span></p>
      <p class="note">Check out our 5-Star reviews on ReviewHub (By Searching for NightEase CPAP)!</p>
      <p class="web">www.NightEaseCPAP.com</p>
    </div>
  </article>

  <article class="panel">
    <div class="inside-copy talk">
      <p class="head">We love to talk.</p>
      <p class="sub">You don't have to be a customer to <strong>call us</strong>, we will answer <strong>any questions</strong> you have!</p>
      <p class="note">Serving all of Ontario.</p>
      <div class="brand"><span class="brand__dot"></span><span class="brand__name">NightEase CPAP</span></div>
    </div>
  </article>

  <article class="panel panel--purple">
    <div class="help">
      <p class="head">When you get diagnosed with obstructive sleep apnea it can be overwhelming.</p>
      <span class="rule"></span>
      <p class="help__label">We are here to <strong>help.</strong><br>We will:</p>
      <ul>
        <li>Visit you in the comfort of your own home so we can privately discuss Sleep Apnea, explain what to expect next, and answer any and all your questions in a relaxed, comfortable environment. You don't get this from any other CPAP Retailer.</li>
        <li>Figure out the best equipment and supplies you need to guarantee your success... We will even set up everything for before we leave so you know it is set up right!</li>
        <li>We are committed to your success. We will spend as much time with you as necessary to make sure all your questions are answered and every concern is addressed.</li>
      </ul>
    </div>
    <div class="help__call">
      <span>Call Us:</span>
      <p class="big-phone">555-014-2290</p>
    </div>
  </article>
</section>

</body>
</html>
```